Feature film needs look book digital brochure - Media/Investor's package

Looking for a designer to create an edgy, eye popping visual representation of my film to get interest from investors, producers and actors, along with Investor and Sponsorship information. Basically it would introduce the project and in about 9-13 pages; give an overview of the film, why to invest, an artistic statement and potential casting ideas and an introduction to the key crew. I have included images (probably more than you need), our film's key art (harbor glass final image & bib logo), and our company (Corvane)'s logo. I've also included samples for another film (tqwl_proposal.pdf) and a proposal I already did for the film. The sample for the other film is more visual and something I'd like to emulate.

The film is called Harbor Glass: a sports drama about two triathletes who overcome their personal demons to train for and compete in the biggest race of their lives.

```html
<!DOCTYPE html>
<html lang="en">
<head>
<meta charset="utf-8">
<title>Harbor Glass – Background &amp; Need</title>
<link rel="stylesheet" href="https://fonts.googleapis.com/css2?family=Carlito:wght@400;700&display=swap">
<style>
  :root {
    --canvas: #ffffff;
    --page-dark: #0a0a0a;
    --photo-mid: #34352f;
    --photo-light: #6d6e63;
    --accent: #d88a2a;
    --text: #f2f2f2;
  }
  * { margin: 0; padding: 0; box-sizing: border-box; }
  html, body { width: 1200px; height: 1000px; overflow: hidden; background: var(--canvas); }
  body { font-family: "Carlito", "Calibri", sans-serif; position: relative; }

  .spread {
    position: absolute; left: 204px; top: 194px; width: 792px; height: 612px;
    background: var(--page-dark); overflow: hidden; color: var(--text);
  }
  .race-photo {
    position: absolute; inset: 0;
    background:
      linear-gradient(90deg, rgba(10,10,10,1) 0%, rgba(10,10,10,0.96) 40%, rgba(10,10,10,0.55) 62%, rgba(10,10,10,0.1) 100%),
      linear-gradient(180deg, #4a4c45 0%, var(--photo-mid) 45%, var(--photo-light) 100%);
  }
  .page-title {
    position: absolute; left: 17px; top: 16px;
    font-weight: 400; font-size: 29px; letter-spacing: 5.2px; color: var(--accent);
  }
  .title-rule {
    position: absolute; left: 0; top: 52px; width: 560px; height: 2px;
    background: linear-gradient(90deg, var(--accent) 0%, var(--accent) 60%, rgba(216,138,42,0) 100%);
  }
  .column {
    position: absolute; top: 70px; width: 162px;
    font-size: 9.1px; line-height: 12.3px;
  }
  .column p { margin-bottom: 6px; }
  .col-1 { left: 17px; }
  .col-2 { left: 188px; }
  .col-3 { left: 363px; }
  .col-4 { left: 533px; }
  .section-heading {
    font-weight: 400; font-size: 18px; line-height: 21px; color: var(--accent);
    margin: 6px 0 4px;
  }
  .page-number {
    position: absolute; left: 759px; top: 588px; width: 18px; height: 18px;
    border: 1px solid var(--text); border-radius: 50%;
    font-size: 10px; line-height: 16px; text-align: center;
  }
</style>
</head>
<body>
<section class="spread">
  <div class="race-photo" role="img" aria-label="Photo of a triathlon race road with runners and a roadside sign marking the half-marathon distance"></div>

  <h1 class="page-title">Background &amp; Need</h1>
  <div class="title-rule"></div>

  <div class="column col-1">
    <p>The idea for Harbor Glass started when Adrian and Marisol, the writers/ producers, went to volunteer at Ridgeline Triathlon in 2010.</p>
    <p>The subject matter is loosely drawn from both of our own personal landscapes. As a participant in triathlons and marathons Adrian has gone through many of the moments that Dorian and Lena, our main characters, go through in their training journey. Of course, true stories come from the heart and many of the emotional moments in Harbor Glass are expressions of questions and feelings both of us have gone through in our lives.</p>
    <p>With our movie, we have a story of two characters: the first is a man with a single-minded focus, who only cares about redeeming himself, not for fame or glory, but for his own fulfillment. The second, a woman who turns to an endurance race to pick up the pieces of what she views as a postponed life of living for the pleasure of others.</p>
    <p>Harbor Glass is a story that unfolds in the emotions we keep from each other and how understanding each other can lead to a greater understanding of ourselves. As a newly married couple, Marisol and Adrian both realize that relationships with people take work, because we are ever-evolving creatures and each of our experiences creates the new version of us.</p>
    <p>This is why we are well positioned to make this movie. Adrian has worked in the film industry for several years, and combined with Marisol’s background in marketing and business management, this new adventure into</p>
  </div>

  <div class="column col-2">
    <p>an independent film making career draws a large parallel with the theme of the film. In making this movie, we are entering the undiscovered country, the future, much like their characters face their own uncertainty throughout the movie.</p>
    <h2 class="section-heading">Approach,<br>Structure &amp; Style</h2>
    <p>Harbor Glass will be an aesthetically bold and sonically rich movie set to a patient pace with action elements and drama surrounding the “chase” of a big race. We will feel the interplay of possibility and realized potential, grounded in human emotion and set against the wonderful backdrop of endurance sports.</p>
    <p>The greatest moments in film happen when a viewer can’t explain what was so beautiful or emotional in a scene, and yet they are moved regardless. It is the energy of a moment that touches people like music. In attempting to express something cinematic, we want to explore, through this film, the intimate details of human feelings and have the audience see those things. But too much of an explanation before this film is made might take away from that. We want to find the cinematic moments that make this movie necessary by itself.</p>
    <p>The look of the film will be very painterly, inspiring, visceral, sexy, with a vibrant color palette. We aim to capture the glitzy, global nature of triathlon and simulate conditions in a variety of countries, using archival footage and using live race footage from real races</p>
  </div>

  <div class="column col-3">
    <p>to add realism to our race scenes. There are dozens of races in British Columbia, the planned hub of our film making, to grab footage and we have relationships with race directors that will facilitate this, with plans to partner with races and triathlon product companies to make the movie authentic.</p>
    <p>With this approach, a mix of traditional and loose film making, we are sprouting seeds and seeing where they grow.</p>
    <p>The film has a large number of exterior scenes, many of which are not weather dependent, and will be filmed around Vancouver, British Columbia. With plans to commence principle photography this fall 2014, the filming can begin without a full budget, and use footage and edits to create sizzle and teaser trailers for more fundraising campaigns throughout filming.</p>
    <p>Our two lead characters each have their own story separate from the other, enabling the practical film making to divide the schedule and film in sections, rather than concentrating all at once. We plan to recruit highly skilled and talented crew and cast members, and work the schedule around other production commitments, in order to facilitate lower wages in exchange for deferrals and profit sharing. The schedule will incorporate several stages of completion, and allow for moments and a feeling of how we want everything to go, but we also are excited about the unknown, the expectation of the unexpected, and how that will rise our story above a sports movie, or a story about inspiration and passion, and be a work that our audience will discuss for years to come.</p>
  </div>

  <div class="column col-4">
    <p>With these considerations, we plan to finish principle photography in Spring, 2015, and present a completed film by the summertime, right in time for triathlon race season!</p>
    <p>A story is a living thing and we are here to parent and guide it to its full-grown life. We both have a great feeling about this story, its need to be told, and we are excited to share this journey with you.</p>
  </div>

  <div class="page-number">4</div>
</section>
</body>
</html>
```